Plakate für Unternehmen im Bereich Kältetechnik
Zielgruppe
Wir sind ein Unternehmen im Bereich Kältetechnik sowohl Wartungen, Service, Überprüfungen als auch Montagen von Split Klimaanlagen. Bei den Klimaanlagen arbeite ich exklusiv nur mit VORTELA zusammen.
Aufgabenstellung
Ergänzung: Das Plakat wir auf einem Regionalen Fußballklub (https://www.kickverband-beispiel.at/verein/8812?SV-Hollbach) neben dem Spielfeld platziert.
Ich habe mir mittels KI eine Idee erstellen lassen. Die Platzierung des Logos und der Schriftzüge ist nicht optimal. Es dient eher als Inspiration für dich.
Ich bin für mutige Designs offen. ABER bitte keine Schneeflocken!! Ich möchte gerne Klimaanlagen in den Mittelpunkt stellen. Dass Banner hat eine größe von länge = 3m höhe = 1m Mein meist verkaufte Produkt ist de VORTELA Luftsanft Klimaanlage: https://www.vortela-beispiel.at/business/klima/luftsanft/

```html
<!DOCTYPE html>
<html lang="de">
<head>
<meta charset="UTF-8">
<title>NORDA KÄLTE – Klimaanlagen Banner</title>
<link href="https://fonts.googleapis.com/css2?family=Plus+Jakarta+Sans:wght@600;700;800&display=swap" rel="stylesheet">
<style>
  :root {
    --page-bg: #e6e6e8;
    --banner-bg: #eeeff2;
    --ink: #161616;
    --brand-blue: #3a43a6;
    --pill-blue: #2e3aa3;
    --pill-blue-end: #2450b0;
    --divider: #3a43a6;
    --photo-light: #f4f4f6;
    --photo-mid: #e2e3e7;
    --photo-dark: #c9cbd2;
  }
  * { margin: 0; padding: 0; box-sizing: border-box; }
  html, body {
    width: 1200px; height: 900px; overflow: hidden;
    background: var(--page-bg);
  }
  body {
    display: flex; align-items: center; justify-content: center;
    font-family: "Plus Jakarta Sans", sans-serif;
  }
  .banner {
    position: relative;
    width: 1140px; height: 380px;
    background: var(--banner-bg);
    overflow: hidden;
  }
  .banner-copy {
    position: absolute; left: 76px; top: 54px;
    z-index: 1;
  }
  .headline {
    font-weight: 800;
    font-size: 72px;
    line-height: 0.98;
    letter-spacing: -0.045em;
    white-space: nowrap;
  }
  .headline-dark { color: var(--ink); display: block; }
  .headline-blue { color: var(--brand-blue); display: block; }
  .subline {
    margin-top: 14px;
    font-weight: 700;
    font-size: 26px;
    letter-spacing: -0.01em;
    color: var(--ink);
    white-space: nowrap;
  }
  .banner-footer {
    position: absolute; left: 76px; top: 300px;
    display: flex; align-items: center;
    z-index: 1;
  }
  .web-pill {
    width: 310px; height: 46px;
    border-radius: 23px;
    background: linear-gradient(90deg, var(--pill-blue), var(--pill-blue-end));
    color: #fff;
    font-weight: 800; font-size: 16px;
    display: flex; align-items: center; justify-content: center;
    white-space: nowrap;
  }
  .logo-row {
    margin-left: 34px;
    display: flex; align-items: center;
    white-space: nowrap;
  }
  .client-mark {
    display: flex; align-items: center; gap: 8px;
    font-weight: 700; font-size: 19px; color: var(--ink);
    letter-spacing: 0.03em;
  }
  .client-mark .dot {
    width: 22px; height: 22px; border-radius: 50%;
    background: var(--ink);
    flex: none;
  }
  .logo-divider {
    width: 1.5px; height: 50px; background: var(--divider);
    margin: 0 16px;
  }
  .partner-mark {
    font-weight: 700; font-size: 23px; color: var(--brand-blue);
    letter-spacing: 0.06em;
  }
  .photo-area {
    position: absolute; right: 0; top: 0;
    width: 320px; height: 100%;
    background: linear-gradient(180deg, var(--photo-light) 0%, var(--photo-mid) 60%, var(--photo-dark) 100%);
    -webkit-mask-image: linear-gradient(90deg, transparent 0, #000 30px);
            mask-image: linear-gradient(90deg, transparent 0, #000 30px);
  }
</style>
</head>
<body>
  <section class="banner">
    <div class="photo-area" role="img" aria-label="Foto: Wand-Klimaanlage an heller Wand, darunter ein Paar, das mit Fernbedienung zum Gerät hinaufblickt"></div>

    <div class="banner-copy">
      <h1 class="headline">
        <span class="headline-dark">Klimaanlagen.</span>
        <span class="headline-blue">Von Profis montiert.</span>
      </h1>
      <p class="subline">Exklusiver VORTELA-Partner in Oberösterreich</p>
    </div>

    <div class="banner-footer">
      <div class="web-pill">www.norda-kaelte-beispiel.at</div>
      <div class="logo-row">
        <div class="client-mark"><span class="dot"></span>NORDA KÄLTE</div>
        <div class="logo-divider"></div>
        <div class="partner-mark">VORTELA</div>
      </div>
    </div>
  </section>
</body>
</html>
```